Biz Cards for Lumivale Associates

Lumivale Associates is seeking a single-sided business card that is more visually-appealing than our current design (see attached).

Notes:
- Our colors are blue & teal.
- Our tag line must be large enough to be easily read
- We don't necessarily need our address included (that's just the biz office)
- We'd like to add our email address: Lumivale512@brindlemail.net

Thanks!

Industry/Entity Type

Business

Contact Information for Business Card

Standard size
PSD file required w/ text on its own layer

Colors
86cfc6
3277b5

```html
<!DOCTYPE html>
<html lang="en">
<head>
<meta charset="utf-8">
<title>Lumivale Associates – Business Card</title>
<link rel="stylesheet" href="https://fonts.googleapis.com/css2?family=Roboto:ital,wght@0,400;0,500;1,400&display=swap">
<style>
  :root {
    --backdrop: #e8e6e3;
    --paper: #f3f3f3;
    --ink: #2c2c2e;
    --brand-blue: #3277b5;
    --brand-teal: #86cfc6;
    --band-start: #2a78bd;
    --band-end: #3a9fc0;
    --band-rule: #dff3f5;
    --card-dark: #231f20;
    --tagline-blue: #2f6fb4;
    --white: #ffffff;
  }
  * { margin: 0; padding: 0; box-sizing: border-box; }
  html, body {
    width: 1200px; height: 960px; overflow: hidden;
    background: var(--backdrop);
    font-family: "Roboto", Arial, sans-serif;
  }
  .canvas { position: relative; width: 1200px; height: 960px; }

  .card { position: absolute; overflow: hidden; }

  /* Front */
  .card-front {
    left: 314px; top: 113px; width: 600px; height: 342px;
    background: var(--paper);
  }
  .front-brand { position: absolute; left: 32px; top: 18px; width: 240px; height: 140px; }
  .brand-dot {
    position: absolute; width: 56px; height: 56px; border-radius: 50%;
    border: 2px solid var(--brand-blue); background: var(--brand-teal);
  }
  .front-brand .brand-dot { left: 92px; top: 2px; }
  .brand-name { color: var(--ink); font-weight: 400; text-align: center; }
  .brand-name .brand-main { display: block; font-size: 30px; letter-spacing: 3px; line-height: 1; }
  .brand-name .brand-sub { display: block; font-size: 13px; letter-spacing: 4px; line-height: 1.2; margin-top: 3px; }
  .front-brand .brand-name { position: absolute; left: 0; top: 62px; width: 240px; }
  .tagline { font-style: italic; color: var(--tagline-blue); font-size: 11px; line-height: 1.2; }
  .front-brand .tagline { position: absolute; left: 0; top: 115px; white-space: nowrap; }

  .contact-band {
    position: absolute; left: 0; top: 163px; width: 600px; height: 163px;
    background: linear-gradient(90deg, var(--band-start), var(--band-end));
    border-bottom: 2px solid var(--band-rule);
  }
  .card-foot { position: absolute; left: 0; top: 326px; width: 600px; height: 16px; background: var(--card-dark); }
  .person { position: absolute; left: 33px; top: 18px; color: var(--white); }
  .person-name { font-size: 20px; font-weight: 500; line-height: 1.2; }
  .person-role { font-size: 14.5px; line-height: 1.3; }
  .contact-list { position: absolute; left: 33px; top: 72px; list-style: none; color: var(--white); font-size: 14px; }
  .contact-list li { display: flex; align-items: center; height: 19px; }
  .contact-list svg { width: 13px; height: 13px; margin-right: 9px; fill: var(--white); }
  .band-accent {
    position: absolute; left: 382px; top: 14px; width: 140px; height: 140px;
    border-radius: 50%; background: var(--brand-teal); opacity: 0.35;
  }

  /* Back */
  .card-back {
    left: 311px; top: 472px; width: 600px; height: 343px;
    background: var(--card-dark);
  }
  .back-brand { position: absolute; left: 0; top: 84px; width: 600px; height: 160px; text-align: center; }
  .back-brand .brand-dot { left: 263px; top: 0; width: 60px; height: 60px; }
  .back-brand .brand-name { position: absolute; left: 0; top: 76px; width: 600px; color: var(--white); }
  .back-brand .brand-main { font-size: 38px; }
  .back-brand .brand-sub { font-size: 16px; letter-spacing: 5px; }
  .back-brand .tagline { position: absolute; left: 0; top: 142px; width: 600px; font-size: 13px; color: var(--brand-blue); }
  .back-web {
    position: absolute; left: 0; top: 288px; width: 600px; text-align: center;
    color: var(--white); font-size: 14px; letter-spacing: 3px;
  }
</style>
</head>
<body>
<div class="canvas">

  <section class="card card-front" aria-label="Business card front">
    <div class="front-brand">
      <span class="brand-dot"></span>
      <div class="brand-name">
        <span class="brand-main">LUMIVALE</span>
        <span class="brand-sub">ASSOCIATES Ltd</span>
      </div>
      <p class="tagline">Bright Minds. Open Hearts. Steady, caring support.</p>
    </div>

    <div class="contact-band">
      <div class="person">
        <p class="person-name">Dana Whitcombe, RN</p>
        <p class="person-role">Mental Health Therapist</p>
      </div>
      <ul class="contact-list">
        <li><svg viewBox="0 0 16 16"><path d="M3 1l3 3-2 2c1 2 3 4 5 5l2-2 3 3-2 3C6 14 2 10 1 3z"/></svg>(855) LUMI-VAL</li>
        <li><svg viewBox="0 0 16 16"><path d="M4 1h7v4H4zM1 6h14v6h-3v3H4v-3H1zM5 10v3h6v-3z"/></svg>(330) 555-0148</li>
        <li><svg viewBox="0 0 16 16"><path d="M1 3h14v10H1zM2 4l6 5 6-5v1L8 10 2 5z" fill-rule="evenodd"/></svg>Lumivale512@brindlemail.net</li>
        <li><svg viewBox="0 0 16 16"><circle cx="8" cy="8" r="7"/><path d="M4 5c2 0 3 1 2 3s1 3 0 5M10 2c0 2 2 2 3 3" stroke="#3a8fc0" stroke-width="1.4" fill="none"/></svg>Lumivale.net</li>
      </ul>
      <span class="band-accent" aria-hidden="true"></span>
    </div>
    <div class="card-foot"></div>
  </section>

  <section class="card card-back" aria-label="Business card back">
    <div class="back-brand">
      <span class="brand-dot"></span>
      <div class="brand-name">
        <span class="brand-main">LUMIVALE</span>
        <span class="brand-sub">ASSOCIATES Ltd</span>
      </div>
      <p class="tagline">Bright Minds. Open Hearts. Steady, caring support.</p>
    </div>
    <p class="back-web">www.Lumivale.net</p>
  </section>

</div>
</body>
</html>
```